Business Card Design Project

We need a business card design for a relatively new company called Lumen Stride. We design paddle (an outdoor winter sport primarily played in the midwest and east coast) and tennis bags for women and men. Lumen Stride is a lifestyle brand for the next generation country club goers. Our bags merge fashion with functionality and are making country club sports trendier and more fashionable.

I would like to include space for
Name: (will fill this in for employees)
Lumen Stride
Phone: (will do this)
Email:
www.lumenstride-example.net

Would also like to include Facebook and Twitter icons.
Please do not use pictures of the bags - this is just to give you an idea of what style bags we sell.

Target Market(s)

30 to 40 year old men and women - luxury market

Industry/Entity Type

Fashion

Requirements
Must have
• Would like the company logo included

```html
<!DOCTYPE html>
<html lang="en">
<head>
<meta charset="utf-8">
<title>Lumen Stride — Business Card</title>
<link href="https://fonts.googleapis.com/css2?family=Great+Vibes&family=Questrial&display=swap" rel="stylesheet">
<style>
  :root {
    --front-bg: #f0eff1;
    --slate: #6a7b7b;
    --slate-dark: #5b6b6c;
    --teal-light: #aec2c2;
    --teal-mid: #8fa8a9;
    --teal-deep: #6f8d8f;
    --ink-white: #f6f6f6;
    --social-a: #57e6d8;
    --social-b: #3f5fd9;
  }
  * { margin: 0; padding: 0; box-sizing: border-box; }
  html, body { width: 1042px; height: 1200px; overflow: hidden; }
  body { background: var(--front-bg); position: relative; font-family: "Questrial", sans-serif; }

  .card-front {
    position: absolute; left: 0; top: 0; width: 1042px; height: 598px;
    background: var(--front-bg);
  }
  .front-brand {
    position: absolute; left: 0; right: 0; top: 255px;
    text-align: center; color: var(--slate);
    font-size: 84px; letter-spacing: 2px;
  }
  .front-url {
    position: absolute; left: 0; right: 0; top: 556px;
    text-align: center; color: var(--slate-dark);
    font-family: "Great Vibes", cursive; font-size: 34px;
  }

  .card-back {
    position: absolute; left: 0; top: 598px; width: 1042px; height: 602px;
    background: radial-gradient(ellipse 520px 300px at 52% 38%, var(--teal-light), var(--teal-mid) 60%, var(--teal-deep));
  }
  .social-links { position: absolute; top: 22px; right: 28px; display: flex; gap: 18px; }
  .social-links span {
    width: 46px; height: 46px; border-radius: 8px; display: block;
  }
  .social-a { background: var(--social-a); }
  .social-b { background: var(--social-b); }

  .wordmark {
    position: absolute; left: 0; right: 0; top: 200px;
    display: flex; align-items: center; justify-content: center; gap: 28px;
    color: var(--ink-white);
  }
  .wordmark-dot { width: 70px; height: 70px; border-radius: 50%; background: var(--ink-white); }
  .wordmark-name { font-size: 88px; letter-spacing: 3px; line-height: 1; }

  .contact {
    position: absolute; left: 47px; top: 420px;
    list-style: none; color: var(--ink-white);
    font-family: "Great Vibes", cursive; font-size: 31px; line-height: 37px;
  }
</style>
</head>
<body>
  <section class="card-front">
    <div class="front-brand">Lumen Stride</div>
    <div class="front-url">www.lumenstride-example.net</div>
  </section>

  <section class="card-back">
    <div class="social-links">
      <span class="social-a" role="img" aria-label="Social network icon"></span>
      <span class="social-b" role="img" aria-label="Social network icon"></span>
    </div>
    <div class="wordmark">
      <span class="wordmark-dot"></span>
      <span class="wordmark-name">Lumen Stride</span>
    </div>
    <ul class="contact">
      <li>Name : (will fill this in for employees)</li>
      <li>Lumen Stride</li>
      <li>Phone : (will do this)</li>
      <li>Email :</li>
    </ul>
  </section>
</body>
</html>
```